Business Card Design

We are an import/export consulting business dealing with all aspects of import/export regulations. Our current design if you look at our website (www.tavrelis.com) are different country flags. It is our business to stay up to date on laws and regulations. We assist companies worldwide. We would like to keep with the flag theme but something different or maybe someone can come up with something totally different that would capture our attention. We are open to suggestions. This design then will transfer over to letterhead, our website, marketing brochures, etc.

Industry/Entity Type

Marketing

Contact Information for Business Card

Dorothy M. Tavrelis, President
Tavrelis Global Advisors, LLC
7 Birchwood Lane,
Millbrook, VT 05601

```html
<!DOCTYPE html>
<html lang="en">
<head>
<meta charset="utf-8">
<title>Tavrelis Global Advisors – Business Card</title>
<link rel="stylesheet" href="https://fonts.googleapis.com/css2?family=Teko:wght@500&family=Open+Sans:wght@600;700&display=swap">
<style>
  :root {
    --backdrop: #a0a0a0;
    --navy: #2e3a78;
    --navy-deep: #121a30;
    --navy-glow: #173063;
    --coral: #ef5a42;
    --white: #ffffff;
    --swoosh: #a7a8ab;
    --edge: #3fd6e0;
  }
  * { margin: 0; padding: 0; box-sizing: border-box; }
  html, body { width: 1200px; height: 1000px; overflow: hidden; }
  body { background: var(--backdrop); position: relative; font-family: "Open Sans", sans-serif; }

  .card { position: absolute; top: 352px; height: 284px; overflow: hidden; }
  .card-front { left: 88px; width: 501px; background: var(--white); }
  .card-back {
    left: 613px; width: 504px;
    background: radial-gradient(ellipse 60% 70% at 48% 35%, var(--navy-glow) 0%, var(--navy-deep) 100%);
    border-right: 2px solid var(--edge);
  }
  .card-art { position: absolute; inset: 0; }

  .brand-name { position: absolute; font-family: "Teko", sans-serif; font-weight: 500; line-height: 0.9; text-align: right; }
  .brand-name .line-main { display: block; letter-spacing: 0.5px; }
  .brand-name .line-sub { display: block; }
  .card-front .brand-name { left: 42px; top: 68px; color: var(--navy); }
  .card-front .brand-name .line-main { font-size: 46px; }
  .card-front .brand-name .line-sub { font-size: 26px; }
  .card-back .brand-name { left: 98px; top: 126px; color: var(--white); }
  .card-back .brand-name .line-main { font-size: 56px; }
  .card-back .brand-name .line-sub { font-size: 30px; }

  .contact { position: absolute; left: 27px; color: var(--navy); }
  .contact-icon { position: absolute; left: 0; width: 10px; height: 12px; }
  .contact-person { top: 196px; }
  .person-name { padding-left: 15px; font-size: 17px; font-weight: 700; color: var(--coral); line-height: 1.1; }
  .person-title { padding-left: 15px; font-size: 11.5px; font-weight: 600; }
  .contact-address { top: 247px; padding-left: 15px; font-size: 13px; font-weight: 600; }
  .contact-person .contact-icon { top: 4px; }
  .contact-address .contact-icon { top: 2px; }
</style>
</head>
<body>

<section class="card card-front" aria-label="Card front">
  <svg class="card-art" viewBox="0 0 501 284" width="501" height="284" aria-hidden="true">
    <defs>
      <radialGradient id="frontNavy" cx="0.85" cy="0.4" r="0.5">
        <stop offset="0" stop-color="#173063"/>
        <stop offset="1" stop-color="#121a30"/>
      </radialGradient>
    </defs>
    <rect width="501" height="284" fill="url(#frontNavy)"/>
    <ellipse cx="100" cy="120" rx="362" ry="228" fill="var(--swoosh)"/>
    <ellipse cx="110" cy="95" rx="360" ry="227" fill="var(--white)"/>
  </svg>

  <div class="brand-name">
    <span class="line-main">TAVRELIS GLOBAL</span>
    <span class="line-sub">Advisors, LLC</span>
  </div>

  <div class="contact contact-person">
    <svg class="contact-icon" viewBox="0 0 10 12" aria-hidden="true">
      <circle cx="5" cy="3" r="2.5" fill="var(--coral)"/>
      <path d="M1 12 V8.5 Q1 6.5 3 6.5 H7 Q9 6.5 9 8.5 V12 Z" fill="var(--coral)"/>
    </svg>
    <p class="person-name">Dorothy M. Tavrelis</p>
    <p class="person-title">President Tavrelis Global Advisors</p>
  </div>

  <div class="contact contact-address">
    <svg class="contact-icon" viewBox="0 0 10 12" aria-hidden="true">
      <path d="M5 0.5 A4 4 0 0 1 9 4.5 C9 7.5 5 11.5 5 11.5 C5 11.5 1 7.5 1 4.5 A4 4 0 0 1 5 0.5 Z M5 3 A1.5 1.5 0 1 0 5 6 A1.5 1.5 0 1 0 5 3 Z" fill="var(--coral)" fill-rule="evenodd"/>
    </svg>
    <p>LLC 7 Birchwood Lane, Millbrook, VT 05601</p>
  </div>
</section>

<section class="card card-back" aria-label="Card back">
  <div class="brand-name">
    <span class="line-main">TAVRELIS GLOBAL</span>
    <span class="line-sub">Advisors, LLC</span>
  </div>
</section>

</body>
</html>
```